Corporate web site design for a blockchain oriented company

Design a web site for Tessaro. The company works on blockchain projects, mostly in B2B . Logo and content of the web site are attached with the project.

Corporate web sites means that we need to present the company and, at least, two of its projects.

Target Market(s)

B2B (Telecom, Gvt, online e-commerce web sites, banks, insurance ...)

Number of Pages Required

3 page

Font styles to use
Sans Serif

Requirements
Must have
• Landing page
• Page for KYC product
• Page for Loyalty product
• Team presentation
• Contact form
• Company presentation
• Several section can be in one page.
Nice to have
• Teaser video per project.
Should not have
• Heavy web site with a lot of animations.

```html
<!DOCTYPE html>
<html lang="en">
<head>
<meta charset="utf-8">
<title>Tessaro – Website Presentation</title>
<link href="https://fonts.googleapis.com/css2?family=Montserrat:wght@400;500;600;700;800&family=Questrial&display=swap" rel="stylesheet">
<style>
  :root {
    --ink: #333333;
    --heading: #444444;
    --white: #ffffff;
    --hero-blue: #2a729f;
    --royal-blue: #0330b9;
    --muted: #a3a3a3;
    --soft-bg: #f8f8f8;
    --pink: #f0357d;
    --field-bg: #f5f5f5;
    --field-line: #ececec;
    --map: #e9ecef;
  }
  * { box-sizing: border-box; margin: 0; padding: 0; }
  html, body { width: 1200px; height: 1200px; overflow: hidden; }
  body { position: relative; font-family: "Montserrat", sans-serif; background: var(--white); color: var(--ink); }

  .quad { position: absolute; width: 600px; height: 600px; overflow: hidden; }
  .quad--tl { left: 0; top: 0; background: var(--white); }
  .quad--tr { left: 600px; top: 0; background: var(--white); }
  .quad--bl { left: 0; top: 600px; background: var(--royal-blue); }
  .quad--br { left: 600px; top: 600px; background: var(--soft-bg); }

  .wordmark { position: absolute; font-family: "Montserrat", sans-serif; font-weight: 600; letter-spacing: 3px; white-space: nowrap; transform: translate(-50%, -50%); line-height: 1; }
  .wordmark--dark { color: var(--ink); }
  .wordmark--light { color: var(--white); }
  .wordmark--tl { left: 300px; top: 300px; font-size: 66px; }
  .wordmark--hero { left: 300px; top: 120px; font-size: 60px; }
  .wordmark--bl { left: 285px; top: 285px; font-size: 66px; }

  /* hero */
  .hero { position: absolute; left: 0; top: 0; width: 600px; height: 337px; background: var(--hero-blue); }
  .hero__tagline { position: absolute; top: 183px; width: 100%; text-align: center; font-size: 7.5px; font-weight: 600; color: var(--white); letter-spacing: 0.3px; }
  .hero__arrow { position: absolute; left: 290px; top: 286px; }

  .section-title { position: absolute; width: 100%; text-align: center; font-weight: 800; font-size: 21px; color: var(--heading); }
  .section-text { position: absolute; text-align: center; font-size: 12px; line-height: 18.5px; color: var(--muted); }

  .about__title { top: 375px; }
  .about__text { top: 420px; left: 92px; width: 416px; }
  .about__btn { position: absolute; left: 235px; top: 511px; width: 103px; height: 28px; border: 1.5px solid var(--pink); color: var(--pink); font-size: 10px; font-weight: 500; display: flex; align-items: center; justify-content: center; }

  /* products */
  .products__title { top: 620px; top: 22px; }
  .products__text { top: 58px; left: 95px; width: 410px; }
  .product { position: absolute; top: 135px; width: 163px; height: 196px; background: var(--white); box-shadow: 0 1px 3px rgba(0,0,0,0.05); }
  .product--kyc { left: 35px; }
  .product--loyalty { left: 210px; }
  .product--team { left: 386px; }
  .product__photo { width: 100%; height: 159px; }
  .product__photo--kyc { background: linear-gradient(135deg, #c9ced6, #4a5a70); }
  .product__photo--loyalty { background: linear-gradient(135deg, #8a8580, #6f6458); }
  .product__photo--team { background: linear-gradient(135deg, #b5b8bb, #7a6a5a); }
  .product__name { height: 37px; display: flex; align-items: center; justify-content: center; font-size: 9.5px; font-weight: 700; color: var(--ink); }

  /* location */
  .map { position: absolute; left: 0; top: 360px; width: 292px; height: 240px; background: linear-gradient(135deg, #eef0f2, var(--map)); }
  .map__card { position: absolute; left: 32px; top: 106px; width: 162px; height: 96px; background: var(--white); padding: 20px 16px 0; }
  .map__pin { position: absolute; left: 17px; top: -16px; width: 30px; height: 30px; border-radius: 50%; background: var(--pink); display: flex; align-items: center; justify-content: center; }
  .map__city { display: inline-block; font-size: 15px; color: var(--ink); padding-bottom: 4px; border-bottom: 1px solid #ddd; white-space: nowrap; }
  .map__address { margin-top: 6px; font-size: 7px; line-height: 9px; color: #999; }
  .map__phone { margin-top: 7px; font-size: 7px; color: var(--pink); }

  /* contact */
  .contact { position: absolute; left: 292px; top: 360px; width: 308px; height: 240px; background: var(--white); }
  .contact__title { position: absolute; left: 0; width: 100%; top: 30px; text-align: center; font-weight: 800; font-size: 21px; color: var(--heading); }
  .field { position: absolute; left: 22px; right: 0; background: var(--field-bg); border: 1px solid var(--field-line); font-size: 7px; color: #999; padding: 7px 10px; }
  .field--name { top: 94px; height: 25px; }
  .field--subject { top: 127px; height: 25px; }
  .field--description { top: 160px; height: 80px; border-bottom: 2px solid var(--pink); }

  .brief { position: absolute; top: 486px; left: 30px; width: 540px; text-align: center; font-family: "Questrial", sans-serif; font-size: 11px; line-height: 20px; color: var(--white); }
</style>
</head>
<body>

  <section class="quad quad--tl">
    <div class="wordmark wordmark--dark wordmark--tl">TESSARO</div>
  </section>

  <section class="quad quad--tr">
    <header class="hero">
      <div class="wordmark wordmark--dark wordmark--hero">TESSARO</div>
      <p class="hero__tagline">WE WILL CRAFT A BEAUTIFUL AND USEFUL FUNCTIONAL EXPERIENCE</p>
      <svg class="hero__arrow" width="20" height="26" viewBox="0 0 20 26" fill="none" stroke="#fff" stroke-width="1.6">
        <line x1="10" y1="2" x2="10" y2="22"/>
        <polyline points="2,14 10,22 18,14"/>
        <line x1="1" y1="25" x2="19" y2="25"/>
      </svg>
    </header>
    <h2 class="section-title about__title">ABOUT TESSARO</h2>
    <p class="section-text about__text">Tessaro is a blockchain company. We build secure B2B products for telecoms, governments, banks and insurers that turn trusted data into simple and reliable experiences.</p>
    <a class="about__btn">Learn More</a>
  </section>

  <section class="quad quad--bl">
    <div class="wordmark wordmark--light wordmark--bl">TESSARO</div>
    <p class="brief">Design a web site for Tessaro. The company works on blockchain projects, mostly in B2B<br>Logo and content of the web site are attached with the project.</p>
  </section>

  <section class="quad quad--br">
    <h2 class="section-title products__title">OUR PRODUCTS</h2>
    <p class="section-text products__text">Tessaro builds blockchain products for business. Meet our KYC and Loyalty platforms and the team behind them</p>

    <article class="product product--kyc">
      <div class="product__photo product__photo--kyc" role="img" aria-label="Photo of a smartphone running an identity verification app"></div>
      <div class="product__name">KYC PRODUCT</div>
    </article>
    <article class="product product--loyalty">
      <div class="product__photo product__photo--loyalty" role="img" aria-label="Photo of hands typing on a laptop keyboard"></div>
      <div class="product__name">LOYALTY PRODUCT</div>
    </article>
    <article class="product product--team">
      <div class="product__photo product__photo--team" role="img" aria-label="Photo of the team working at a laptop on a wooden desk"></div>
      <div class="product__name">OUR TEAM</div>
    </article>

    <div class="map" role="img" aria-label="Street map around the office location">
      <div class="map__card">
        <span class="map__pin">
          <svg width="12" height="14" viewBox="0 0 12 14"><path d="M6 0C2.7 0 0 2.6 0 5.8 0 10 6 14 6 14s6-4 6-8.2C12 2.6 9.3 0 6 0z" fill="#fff"/><circle cx="6" cy="5.6" r="2" fill="#f0357d"/></svg>
        </span>
        <div class="map__city">Marlow Bay</div>
        <p class="map__address">412 Harbor Lane<br>Westbrook, ME 04092</p>
        <p class="map__phone">+1 555 0142 368</p>
      </div>
    </div>

    <div class="contact">
      <h2 class="contact__title">CONTACT US</h2>
      <div class="field field--name">Your Name</div>
      <div class="field field--subject">Subject</div>
      <div class="field field--description">Description</div>
    </div>
  </section>

</body>
</html>
```